BrindleStaffing Business Card Design

We are a staffing company finding positions for dedicated nurses and physicians.

Target Market(s)

Business Professionals

Industry/Entity Type

Staffing

Contact Information for Business Card

Gregory Malden
Chairman
417 39th Crescent South
SAINT PETERSBURG FL 33719
813-555-0147 Mobile
813-555-0183 Fax
gmalden@brindlestaffing.example
www.brindlestaffing.example

Font styles to use
Sans Serif

Colors
fbee3e
f04a50
f37122

Requirements
Must have
• Logo Attached, see colors below. We'd like to see Yellow, Orange and Red.

```html
<!DOCTYPE html>
<html lang="en">
<head>
<meta charset="utf-8">
<title>BrindleStaffing Business Card</title>
<link rel="stylesheet" href="https://fonts.googleapis.com/css2?family=Work+Sans:wght@400;500;600&display=swap">
<style>
  :root {
    --page-bg: #e6e6e6;
    --card-white: #ffffff;
    --brand-yellow: #fbee3e;
    --brand-red: #f04a50;
    --brand-orange: #f37122;
    --brand-red-deep: #d93a40;
    --text-grey: #555a60;
    --font-main: "Work Sans", Arial, sans-serif;
  }
  * { box-sizing: border-box; margin: 0; padding: 0; }
  html, body {
    width: 1200px; height: 900px; overflow: hidden;
    background: var(--page-bg);
    font-family: var(--font-main);
  }
  .canvas { position: relative; width: 1200px; height: 900px; }
  .card {
    position: absolute; left: 250px; width: 700px; height: 400px;
    box-shadow: 0 6px 18px rgba(0,0,0,0.18);
    overflow: hidden;
  }
  .card-front { top: 30px; background: var(--card-white); }
  .card-back {
    top: 470px;
    background: radial-gradient(ellipse at 40% 60%, var(--brand-orange) 0%, var(--brand-red) 60%, var(--brand-red-deep) 100%);
    display: flex; align-items: center; justify-content: center;
  }
  .brand-name {
    position: absolute; top: 44px; right: 46px;
    font-size: 34px; font-weight: 600; color: var(--brand-orange);
    letter-spacing: -0.5px;
  }
  .holder { position: absolute; left: 38px; top: 150px; }
  .holder-name { font-size: 26px; font-weight: 500; letter-spacing: 3px; }
  .holder-name .first { color: var(--brand-orange); }
  .holder-name .last { color: var(--brand-red); }
  .holder-title { font-size: 15px; color: var(--text-grey); letter-spacing: 1px; margin-top: 2px; }
  .divider {
    position: absolute; left: 38px; right: 38px; top: 220px;
    height: 1.5px; background: var(--brand-red);
  }
  .contact-list { position: absolute; left: 38px; top: 234px; list-style: none; }
  .contact-list li {
    display: flex; align-items: center; gap: 12px;
    font-size: 15px; color: var(--text-grey); letter-spacing: 1px;
    height: 24px;
  }
  .contact-list svg { width: 12px; height: 12px; flex: none; }
  .contact-list .label { font-size: 12px; color: var(--brand-orange); letter-spacing: 1px; }
  .contact-list .highlight { color: var(--brand-red); font-weight: 500; }
  .address {
    position: absolute; right: 38px; top: 250px; text-align: right;
    font-size: 14px; color: var(--text-grey); letter-spacing: 1.5px; line-height: 22px;
  }
  .bottom-band { position: absolute; left: 0; bottom: 0; width: 700px; height: 400px; }
  .back-brand { font-size: 72px; font-weight: 600; color: var(--card-white); letter-spacing: -1px; }
</style>
</head>
<body>
<main class="canvas">
  <section class="card card-front" aria-label="Business card front">
    <div class="brand-name">BrindleStaffing</div>

    <div class="holder">
      <div class="holder-name"><span class="first">GREGORY</span> <span class="last">MALDEN</span></div>
      <div class="holder-title">Chairman</div>
    </div>

    <div class="divider"></div>

    <ul class="contact-list">
      <li>
        <svg viewBox="0 0 12 12" aria-hidden="true"><path d="M2.5 1 L4.5 1 L5 3.5 L3.8 4.5 C4.5 6 6 7.5 7.5 8.2 L8.5 7 L11 7.5 L11 9.5 C11 10.3 10.3 11 9.5 11 C5 11 1 7 1 2.5 C1 1.7 1.7 1 2.5 1 Z" fill="var(--brand-orange)"/></svg>
        <span>813-555-0147 <span class="label">Mobile</span></span>
      </li>
      <li>
        <svg viewBox="0 0 12 12" aria-hidden="true"><rect x="3" y="1" width="6" height="3.5" fill="none" stroke="var(--brand-orange)" stroke-width="1.2"/><rect x="1" y="4.5" width="10" height="4.5" fill="var(--brand-orange)"/><rect x="3" y="8" width="6" height="3" fill="#fff" stroke="var(--brand-orange)" stroke-width="1.1"/></svg>
        <span>813-555-0183 <span class="label">Fax</span></span>
      </li>
      <li>
        <svg viewBox="0 0 12 12" aria-hidden="true"><rect x="1" y="2.5" width="10" height="7" fill="none" stroke="var(--brand-orange)" stroke-width="1.3"/><path d="M1 2.5 L6 6.5 L11 2.5" fill="none" stroke="var(--brand-orange)" stroke-width="1.3"/></svg>
        gmalden@brindlestaffing.example
      </li>
      <li>
        <svg viewBox="0 0 12 12" aria-hidden="true"><circle cx="6" cy="6" r="5" fill="none" stroke="var(--brand-orange)" stroke-width="1.2"/><ellipse cx="6" cy="6" rx="2.2" ry="5" fill="none" stroke="var(--brand-orange)" stroke-width="1"/><path d="M1 6 H11 M2 3.5 H10 M2 8.5 H10" stroke="var(--brand-orange)" stroke-width="0.9"/></svg>
        <span>www.<span class="highlight">brindlestaffing</span>.example</span>
      </li>
    </ul>

    <div class="address">
      417 39th Crescent South<br>
      SAINT PETERSBURG FL 33719
    </div>

    <svg class="bottom-band" viewBox="0 0 700 400" aria-hidden="true">
      <path d="M0 386 L430 356 C470 353 480 322 530 318 L700 310 L700 400 L0 400 Z" fill="var(--brand-red)"/>
      <path d="M0 376 L430 346 C448 345 458 340 468 332" fill="none" stroke="var(--brand-yellow)" stroke-width="4"/>
    </svg>
  </section>

  <section class="card card-back" aria-label="Business card back">
    <div class="back-brand">BrindleStaffing</div>
  </section>
</main>
</body>
</html>
```